Facial whitening product needs a packaging design

We need a packaging design for our new product named LUMIVOR Ultra-Bright Treatment. (btw Lumivor is our brand name). We want a package to look like a high end whitening treatment and eye-kicking. Here is the dimension for the labels and the dimensions the bottle for making a box is hight 5cm width 8 cm for the label (almost around the bottle) and 9.5 cm hight and 2.7 radius for a bottle (15ml) but we think we need a big box (the example is attached for the size and pattern of the box but not for the design) but the design is not fixed and all up to the designer.

Target Market(s)

Online shopper and mass targeted but the product need to look high end.

Industry/Entity Type

Product

Font styles to use
Sans Serif

Colors
34b8a4
ffffff

Requirements
Must have
• eye-kicking box that looks high end. I think white box would be great (file attached for example) and white bottle would be great but if you come with better idea then you can change it.
Nice to have
• You should look at Vitamin c box that a attached for an inspiration
• But the design is now free-style

```html
<!DOCTYPE html>
<html lang="en">
<head>
<meta charset="utf-8">
<title>LUMIVOR Ultra-Bright Treatment – Packaging</title>
<link href="https://fonts.googleapis.com/css2?family=Montserrat:wght@300;400;600;700&display=swap" rel="stylesheet">
<style>
  :root{
    --teal:#02a89c;
    --teal-soft:#34b8a4;
    --white:#ffffff;
    --ink:#2b2b2b;
    --grey:#555b5e;
    --label-grey:#4a4f52;
    --silver-a:#9fa2a4;
    --silver-b:#e6e7e8;
    --bg-a:#dfe9eb;
    --bg-b:#ffffff;
  }
  *{box-sizing:border-box;margin:0;padding:0}
  html,body{width:1200px;height:1000px;overflow:hidden}
  body{
    font-family:'Montserrat',sans-serif;
    background:radial-gradient(ellipse at 20% 10%,var(--bg-a) 0%,#eef3f4 45%,var(--bg-b) 90%);
    position:relative;color:var(--ink);
  }
  .abs{position:absolute}
  .caption{font-size:18px;font-weight:300;color:var(--label-grey)}

  /* Outer box front panel */
  .outer-box{left:30px;top:222px;width:615px;height:600px;background:var(--teal);overflow:hidden}
  .outer-box .brand{top:68px;left:0;width:100%;text-align:center;color:var(--white);font-size:54px;font-weight:300;letter-spacing:2px}
  .silver-band{top:146px;left:0;width:100%;height:42px;background:linear-gradient(90deg,var(--silver-a),var(--silver-b) 50%,var(--silver-a));text-align:center;font-size:31px;line-height:42px;color:var(--ink);font-weight:400}
  .silver-band b{font-weight:700}
  .outer-box .sub{top:196px;left:0;width:100%;text-align:center;color:var(--white);font-size:17px;letter-spacing:5px;font-weight:400}

  /* Flat label panels */
  .panel{width:134px;border:1px solid #d9dcdd;background:var(--white);overflow:hidden}
  .panel-1{left:742px;top:15px;height:468px}
  .panel-2{left:743px;top:510px;height:466px}
  .vertical{writing-mode:vertical-rl;transform:rotate(180deg);white-space:nowrap}
  .panel-1 .brand{left:22px;top:66px;font-size:50px;font-weight:300;color:var(--ink);letter-spacing:1px}
  .panel-1 .product{left:80px;top:70px;font-size:13px;color:var(--grey);border-left:1px solid var(--grey);padding-left:3px}
  .chip{left:0;width:100%;text-align:center;background:var(--teal);color:var(--white)}
  .panel-1 .chip{top:343px;height:24px;line-height:24px;font-size:15px}
  .panel-1 .chip b{font-weight:700}
  .claim{left:0;width:100%;text-align:center;font-size:11px;line-height:16px;color:var(--grey)}
  .panel-1 .claim{top:404px}

  .panel-2 .teal-top{left:0;top:0;width:100%;height:334px;background:var(--teal)}
  .panel-2 .brand{left:38px;top:30px;font-size:52px;font-weight:300;color:var(--white);letter-spacing:1px}
  .panel-2 .grey-band{left:0;top:334px;width:100%;height:22px;background:linear-gradient(90deg,var(--silver-a),var(--silver-b));text-align:center;line-height:22px;font-size:15px;color:var(--ink)}
  .panel-2 .grey-band b{font-weight:700}
  .panel-2 .sub{left:0;top:360px;width:100%;text-align:center;font-size:10px;letter-spacing:2px;color:var(--teal)}
  .panel-2 .note{left:0;top:396px;width:100%;text-align:center;font-size:9px;line-height:13px;color:var(--grey)}
  .panel-2 .claim{top:428px;left:8px;width:118px;font-size:9px;line-height:12px;border-top:1px solid var(--grey);border-bottom:1px solid var(--grey);padding:2px 0}

  /* Bottles */
  .bottle{display:flex;flex-direction:column;align-items:center}
  .bottle .cap{width:100%;border-radius:6px 6px 2px 2px;background:linear-gradient(90deg,#d7dbdc,#f4f6f6 45%,#cfd4d5);opacity:.9;position:relative}
  .bottle .pump{position:absolute;left:30%;top:10%;width:40%;height:55%;background:linear-gradient(90deg,#eceeee,#fff,#e2e5e5);border-radius:3px}
  .bottle .ring{width:100%;height:7px;background:linear-gradient(180deg,#6c7073,#e9eaeb 50%,#5e6265)}
  .bottle .body{width:100%;flex:1;background:linear-gradient(90deg,#e7eaea,#ffffff 40%,#f4f5f5 70%,#dfe2e2);border-radius:0 0 12px 12px;display:flex;flex-direction:column;align-items:center;justify-content:flex-end}
  .bottle .mark{color:var(--ink);font-weight:300;letter-spacing:1px}
  .bottle .band{width:100%;background:var(--teal);color:var(--white);text-align:center}
  .bottle .band b{font-weight:700}
  .bottle .tiny{color:var(--teal);letter-spacing:1px;text-align:center}
  .bottle .small{color:var(--grey);text-align:center}
  .bottle .ruled{border-top:1px solid var(--grey);border-bottom:1px solid var(--grey);width:80%;color:var(--grey);text-align:center}

  .bottle-box{left:295px;top:470px;width:84px;height:330px}
  .bottle-box .cap{height:46px}
  .bottle-box .body{padding-bottom:18px}
  .bottle-box .mark{font-size:20px;margin-bottom:12px}
  .bottle-box .band{font-size:9px;line-height:14px}
  .bottle-box .tiny{font-size:5px;margin:1px 0 6px}
  .bottle-box .small{font-size:5px;line-height:7px;margin-bottom:3px}
  .bottle-box .ruled{font-size:5px;line-height:7px}

  .bottle-1{left:933px;top:118px;width:98px;height:356px}
  .bottle-1 .cap{height:90px}
  .bottle-1 .body{padding-bottom:40px}
  .bottle-1 .mark-row{display:flex;align-items:flex-start;margin-bottom:12px}
  .bottle-1 .mark{font-size:22px}
  .bottle-1 .mark-sub{font-size:7px;color:var(--grey);border-left:1px solid var(--grey);padding-left:2px;margin-left:2px}
  .bottle-1 .band{font-size:7px;line-height:16px}
  .bottle-1 .small{font-size:7px;line-height:11px;margin-top:6px}

  .bottle-2{left:932px;top:614px;width:98px;height:358px}
  .bottle-2 .cap{height:86px}
  .bottle-2 .body{padding-bottom:28px}
  .bottle-2 .mark{font-size:22px;margin-bottom:14px}
  .bottle-2 .band{font-size:11px;line-height:16px}
  .bottle-2 .tiny{font-size:6px;margin:2px 0 8px}
  .bottle-2 .small{font-size:6px;line-height:8px;margin-bottom:4px}
  .bottle-2 .ruled{font-size:6px;line-height:8px}
</style>
</head>
<body>

  <!-- Outer box -->
  <section class="abs outer-box" aria-label="Outer box front">
    <div class="abs brand">LUMIVOR</div>
    <div class="abs silver-band"><b>ULTRA</b>-BRIGHT</div>
    <div class="abs sub">TREATMENT</div>
  </section>
  <div class="abs bottle bottle-box">
    <div class="cap"><div class="pump"></div></div>
    <div class="ring"></div>
    <div class="body">
      <div class="mark vertical">LUMIVOR</div>
      <div class="band"><b>ULTRA</b>-BRIGHT</div>
      <div class="tiny">TREATMENT</div>
      <div class="small">for a brighter,<br>more radiant complexion</div>
      <div class="ruled">LIGHTEN SKIN TONE<br>&amp; REDUCE DARK SPOTS</div>
    </div>
  </div>
  <p class="abs caption" style="left:32px;top:836px">OUTER BOX</p>

  <!-- Option 1 -->
  <section class="abs panel panel-1" aria-label="Label option 1">
    <div class="abs brand vertical">LUMIVOR</div>
    <div class="abs product vertical">ULTRA-BRIGHT TREATMENT</div>
    <div class="abs chip"><b>ANTI</b>-AGING</div>
    <div class="abs claim">LIGHTEN SKIN TONE<br>&amp; REDUCE DARK SPOTS</div>
  </section>
  <p class="abs caption" style="left:932px;top:78px">Option1</p>
  <div class="abs bottle bottle-1">
    <div class="cap"><div class="pump"></div></div>
    <div class="ring"></div>
    <div class="body">
      <div class="mark-row">
        <div class="mark vertical">LUMIVOR</div>
        <div class="mark-sub vertical">ULTRA-BRIGHT TREATMENT</div>
      </div>
      <div class="band">UVA / UVB FILTERS</div>
      <div class="small">for a brighter,<br>more radiant complexion</div>
    </div>
  </div>

  <!-- Option 2 -->
  <section class="abs panel panel-2" aria-label="Label option 2">
    <div class="abs teal-top"></div>
    <div class="abs brand vertical">LUMIVOR</div>
    <div class="abs grey-band"><b>ULTRA</b>-BRIGHT</div>
    <div class="abs sub">TREATMENT</div>
    <div class="abs note">for a brighter,<br>more radiant complexion</div>
    <div class="abs claim">LIGHTEN SKIN TONE<br>&amp; REDUCE DARK SPOTS</div>
  </section>
  <p class="abs caption" style="left:948px;top:578px">Option2</p>
  <div class="abs bottle bottle-2">
    <div class="cap"><div class="pump"></div></div>
    <div class="ring"></div>
    <div class="body">
      <div class="mark vertical">LUMIVOR</div>
      <div class="band"><b>ULTRA</b>-BRIGHT</div>
      <div class="tiny">TREATMENT</div>
      <div class="ruled">LIGHTEN SKIN TONE<br>&amp; REDUCE DARK SPOTS</div>
    </div>
  </div>

</body>
</html>
```